Business Card Design Project

Bold, modern, clean business card design needed. Prefer double sided with art logo on the back. Front of card with company name logo, no art.

Target Market(s)

Our consulting company supports local, state and federal law enforcement officers. Therefore the design should be clean and direct with no flash or arrogance to it.

Industry/Entity Type

Business

```html
<!DOCTYPE html>
<html lang="en">
<head>
<meta charset="utf-8">
<title>Halvard Consulting – Business Cards</title>
<link href="https://fonts.googleapis.com/css2?family=Open+Sans:ital,wght@0,400;0,600;1,400&display=swap" rel="stylesheet">
<style>
  :root {
    --page-bg: #d9d9d9;
    --card-white: #ffffff;
    --brand-green: #97c80a;
    --ink-black: #111111;
    --panel-black: #0d0d0d;
    --text-light: #f2f2f2;
  }
  * { box-sizing: border-box; margin: 0; padding: 0; }
  html, body {
    width: 1200px; height: 1023px; overflow: hidden;
    background: var(--page-bg);
    font-family: "Open Sans", Arial, sans-serif;
  }
  .sheet { position: relative; width: 1200px; height: 1023px; }
  .card {
    position: absolute; top: 214px;
    width: 340px; height: 595px;
    background: var(--card-white);
    box-shadow: 0 6px 18px rgba(0,0,0,0.18);
    overflow: hidden;
  }
  .card--front { left: 180px; }
  .card--back { left: 680px; }

  .name-tab {
    position: absolute; top: 0; right: 28px;
    width: 232px; height: 140px;
    background: var(--brand-green);
    border-radius: 0 0 14px 14px;
    display: flex; flex-direction: column; align-items: center; justify-content: center;
    color: var(--ink-black);
  }
  .name-tab__name { font-size: 27px; font-weight: 400; line-height: 1.1; }
  .name-tab__role { font-size: 18px; font-style: italic; }

  .wordmark {
    position: absolute; left: 0; right: 0;
    padding: 0 20px;
    display: flex; align-items: center; justify-content: center; gap: 9px;
    color: var(--ink-black);
    font-weight: 600; letter-spacing: 0.5px;
    white-space: nowrap;
    font-size: 20px;
  }
  .wordmark__dot {
    width: 16px; height: 16px; border-radius: 50%;
    background: var(--brand-green); flex: none;
  }
  .card--front .wordmark { top: 220px; }
  .card--back .wordmark { top: 284px; }

  .contact-panel {
    position: absolute; left: 0; top: 340px;
    width: 290px; height: 168px;
    background: var(--panel-black);
    border-radius: 0 14px 14px 0;
    padding: 34px 0 0 26px;
    display: flex; flex-direction: column; gap: 14px;
  }
  .contact-line {
    display: flex; align-items: center; gap: 10px;
    color: var(--text-light); font-size: 16px;
    white-space: nowrap;
  }
  .contact-line__icon {
    width: 18px; height: 18px; flex: none;
    background: var(--brand-green); border-radius: 3px;
    display: flex; align-items: center; justify-content: center;
  }
</style>
</head>
<body>
<main class="sheet">

  <section class="card card--front" aria-label="Card front">
    <div class="name-tab">
      <p class="name-tab__name">Daniel Brooks</p>
      <p class="name-tab__role">Director</p>
    </div>

    <div class="wordmark">
      <span class="wordmark__dot"></span>
      <span>HALVARD CONSULTING</span>
    </div>

    <div class="contact-panel">
      <p class="contact-line">
        <span class="contact-line__icon">
          <svg width="12" height="12" viewBox="0 0 12 12"><rect x="3.5" y="1" width="5" height="10" rx="1" fill="none" stroke="#fff" stroke-width="1.2"/><circle cx="6" cy="9.3" r="0.6" fill="#fff"/></svg>
        </span>
        +44(0)0800 555 0190
      </p>
      <p class="contact-line">
        <span class="contact-line__icon">
          <svg width="12" height="12" viewBox="0 0 12 12"><circle cx="6" cy="6" r="4.5" fill="none" stroke="#fff" stroke-width="1.1"/><ellipse cx="6" cy="6" rx="2" ry="4.5" fill="none" stroke="#fff" stroke-width="1"/><line x1="1.5" y1="6" x2="10.5" y2="6" stroke="#fff" stroke-width="1"/></svg>
        </span>
        www.halvardconsult.com
      </p>
      <p class="contact-line">
        <span class="contact-line__icon">
          <svg width="12" height="12" viewBox="0 0 12 12"><rect x="1.5" y="3" width="9" height="6" fill="none" stroke="#fff" stroke-width="1.1"/><polyline points="1.5,3 6,6.5 10.5,3" fill="none" stroke="#fff" stroke-width="1.1"/></svg>
        </span>
        dbrooks@halvardconsult.com
      </p>
    </div>
  </section>

  <section class="card card--back" aria-label="Card back">
    <div class="wordmark">
      <span class="wordmark__dot"></span>
      <span>HALVARD CONSULTING</span>
    </div>
  </section>

</main>
</body>
</html>
```